FLYER: Lighting Geometry at Rural Junctions - Review of Signage Placement - training

We are hosting a class in Australia 30, November to 4, December 2020. I would like to have a flyer designed to "sell" the class with description of course topics. I have uploaded a flyer I started on my own but I want it to be professional. Dr. Brenlow only gets to AU every 3-5 years to teach from the US. I would like to have some type of roadway scenery, prefer a nighttime scene.

Target Market(s)

Accident reconstructionists and engineers, police reconstructionists.

Font styles to use
Serif

Colors
fec214

Requirements
Must have
• Name of course and course topics, location of course, price, website and contact information.
Nice to have
• Some type of roadway background, possibly a nighttime scene on a roadway.

```html
<!DOCTYPE html>
<html lang="en">
<head>
<meta charset="utf-8">
<title>Lighting Geometry at Rural Junctions – Course Flyer</title>
<link rel="stylesheet" href="https://fonts.googleapis.com/css2?family=Poppins:wght@400;500;600;700;800&display=swap">
<style>
  :root {
    --canvas: #ececec;
    --paper: #f1f1f2;
    --night-deep: #0f1a2e;
    --night-mid: #24324a;
    --night-glow: #6b4a3a;
    --amber: #e09a17;
    --title-yellow: #fec214;
    --heading-orange: #f0641e;
    --ink: #2e2e2e;
    --ink-soft: #4a4a4a;
    --white: #ffffff;
    --black: #141414;
  }
  * { margin: 0; padding: 0; box-sizing: border-box; }
  html, body { width: 1200px; height: 1000px; overflow: hidden; background: var(--canvas); }
  body { position: relative; font-family: "Poppins", sans-serif; }

  .flyer {
    position: absolute; left: 260px; top: 19px;
    width: 831px; height: 1175px;
    transform: scale(0.8187); transform-origin: top left;
    background: var(--paper); overflow: hidden;
    box-shadow: 0 2px 10px rgba(0,0,0,.12);
  }
  .flyer svg.layer { position: absolute; inset: 0; width: 831px; height: 1175px; }

  .brand {
    position: absolute; right: 44px; top: 22px; text-align: right;
    font-weight: 800; color: var(--black); line-height: 1;
  }
  .brand__line1 { display: block; font-size: 50px; letter-spacing: 1px; }
  .brand__line2 { display: block; font-size: 26px; margin-top: 6px; }

  .headline { position: absolute; right: 18px; top: 244px; text-align: right; }
  .headline__line {
    display: inline-block; background: var(--black); color: var(--white);
    font-weight: 800; font-size: 40px; line-height: 50px; padding: 0 8px;
    text-transform: uppercase; letter-spacing: .3px;
  }
  .headline__row { display: block; }
  .headline__row--2 { margin-right: 6px; }
  .headline__row--3 { margin-right: 150px; }
  .headline__row--4 { margin-right: 12px; }

  .edition { position: absolute; right: 70px; top: 448px; text-align: right;
    color: var(--title-yellow); font-weight: 500; font-size: 42px; line-height: 46px; }
  .edition span { display: block; }
  .edition span:first-child { margin-right: 88px; }

  .presenter-photo { position: absolute; left: 33px; top: 303px; width: 236px; height: 236px; }

  .intro { position: absolute; left: 35px; top: 555px; width: 430px; color: var(--ink); }
  .intro__name { font-weight: 700; font-size: 20px; line-height: 25px; }
  .intro__text { font-weight: 400; font-size: 20px; line-height: 25px; color: var(--ink-soft); margin-top: 8px; }

  .details { position: absolute; left: 35px; top: 715px; width: 470px; color: var(--ink); }
  .details__heading { color: var(--heading-orange); font-weight: 800; font-size: 27px; line-height: 32px; }
  .details__text { font-weight: 700; font-size: 19px; line-height: 24px; }
  .details__text--web { font-size: 20px; }
  .details__block { margin-bottom: 32px; }
  .details__block--fee { margin-bottom: 30px; }
  .details__contact { font-weight: 500; font-size: 20px; line-height: 30px; display: flex; align-items: center; gap: 6px; }
  .details__contact svg { width: 18px; height: 18px; }

  .about { position: absolute; left: 35px; top: 1106px; font-size: 15px; line-height: 20px; color: var(--ink-soft); }

  .topics { position: absolute; left: 518px; top: 672px; width: 298px; color: var(--white); }
  .topics__title { font-weight: 800; font-size: 34px; line-height: 40px; margin-bottom: 6px; }
  .topics__list { list-style: none; }
  .topics__item { display: flex; gap: 5px; font-size: 13.6px; line-height: 16.5px; font-weight: 500; letter-spacing: -0.15px; margin-bottom: 4.5px; }
  .topics__item svg { flex: 0 0 15px; width: 15px; height: 15px; margin-top: 1px; }
</style>
</head>
<body>
<article class="flyer">
  <svg class="layer" viewBox="0 0 831 1175" aria-hidden="true">
    <polygon points="0,250 700,660 0,1175" fill="#e7e8ea"/>
    <polygon points="0,600 420,1175 0,1175" fill="#ebebed"/>
    <polygon points="150,650 480,800 300,1175" fill="#f5f5f6"/>
    <polygon points="500,0 831,0 831,128 310,160" fill="#d9dadd"/>
    <polygon points="520,590 831,540 831,1175 415,1175" fill="var(--amber)"/>
    <polygon points="715,1175 831,1100 831,1175" fill="#f3f3f3"/>
  </svg>

  <svg class="layer" viewBox="0 0 831 1175" role="img" aria-label="Night-time multilane highway with city lights and red and white light trails">
    <defs>
      <linearGradient id="nightRoad" x1="0" y1="0" x2="1" y2="1">
        <stop offset="0" stop-color="#1c2436"/>
        <stop offset=".45" stop-color="var(--night-mid)"/>
        <stop offset=".7" stop-color="var(--night-glow)"/>
        <stop offset="1" stop-color="var(--night-deep)"/>
      </linearGradient>
    </defs>
    <polygon points="0,0 500,0 310,160 831,128 831,460 700,660 0,290" fill="url(#nightRoad)"/>
  </svg>

  <div class="brand">
    <span class="brand__line1">ROADLINE</span>
    <span class="brand__line2">SAFETY GROUP</span>
  </div>

  <h1 class="headline">
    <span class="headline__row"><span class="headline__line">Lighting Geometry at</span></span>
    <span class="headline__row headline__row--2"><span class="headline__line">Rural Junctions,</span></span>
    <span class="headline__row headline__row--3"><span class="headline__line">Review of</span></span>
    <span class="headline__row headline__row--4"><span class="headline__line">Signage Placement</span></span>
  </h1>

  <p class="edition"><span>OPEN CLASS</span><span>SEACLIFF NSW</span></p>

  <svg class="presenter-photo" viewBox="0 0 236 236" role="img" aria-label="Portrait photo of presenter Dr. Colin Brenlow">
    <circle cx="118" cy="118" r="116" fill="#e4e6e2" stroke="#dcdfd8" stroke-width="4"/>
    <circle cx="118" cy="118" r="110" fill="#cfc9c3"/>
  </svg>

  <section class="intro">
    <p class="intro__name">Presented by: Colin Brenlow Ph.D.<br>World renowned Human Factors expert</p>
    <p class="intro__text">It has been 3 years since Dr. Brenlow has come to AU to teach, don’t miss out on this year’s class.</p>
  </section>

  <section class="details">
    <div class="details__block">
      <h2 class="details__heading">Location:</h2>
      <p class="details__text">Harbourview Lodge – Coastal Reserve<br>12 Headland Road, Seacliff NSW</p>
    </div>
    <div class="details__block details__block--fee">
      <h2 class="details__heading">Course Fee</h2>
      <p class="details__text">$1,730 AU / $1,200 USD</p>
    </div>
    <div>
      <h2 class="details__heading">Register on our website:</h2>
      <p class="details__text details__text--web">www.roadlinesafety.com<br>or Contact:</p>
      <p class="details__contact">
        <svg viewBox="0 0 18 18"><rect x="4" y="1" width="10" height="16" rx="2" fill="none" stroke="#333" stroke-width="1.5"/><line x1="8" y1="14.5" x2="10" y2="14.5" stroke="#333" stroke-width="1.5"/></svg>
        555-014-2290
      </p>
      <p class="details__contact">
        <svg viewBox="0 0 18 18"><rect x="1.5" y="4" width="15" height="10" fill="none" stroke="#333" stroke-width="1.3"/><polyline points="1.5,4 9,10 16.5,4" fill="none" stroke="#333" stroke-width="1.3"/></svg>
        info@roadlinesafety.com
      </p>
    </div>
  </section>

  <p class="about">Visit www.RoadlineResearch.com/about/<br>to learn more about Dr. Brenlow</p>

  <section class="topics">
    <h2 class="topics__title">Course Topics</h2>
    <ul class="topics__list">
      <li class="topics__item"><svg viewBox="0 0 15 15"><circle cx="7.5" cy="7.5" r="6.5" fill="none" stroke="#fff" stroke-width="1.3"/><polyline points="4.3,7.7 6.6,10 10.8,5" fill="none" stroke="#fff" stroke-width="1.5"/></svg>Perception-Response Time</li>
      <li class="topics__item"><svg viewBox="0 0 15 15"><circle cx="7.5" cy="7.5" r="6.5" fill="none" stroke="#fff" stroke-width="1.3"/><polyline points="4.3,7.7 6.6,10 10.8,5" fill="none" stroke="#fff" stroke-width="1.5"/></svg>Response to slow moving or stopped vehicles on multilane high speed roads</li>
      <li class="topics__item"><svg viewBox="0 0 15 15"><circle cx="7.5" cy="7.5" r="6.5" fill="none" stroke="#fff" stroke-width="1.3"/><polyline points="4.3,7.7 6.6,10 10.8,5" fill="none" stroke="#fff" stroke-width="1.5"/></svg>Nighttime recognition</li>
      <li class="topics__item"><svg viewBox="0 0 15 15"><circle cx="7.5" cy="7.5" r="6.5" fill="none" stroke="#fff" stroke-width="1.3"/><polyline points="4.3,7.7 6.6,10 10.8,5" fill="none" stroke="#fff" stroke-width="1.5"/></svg>Headlight mapping demonstration and instruction</li>
      <li class="topics__item"><svg viewBox="0 0 15 15"><circle cx="7.5" cy="7.5" r="6.5" fill="none" stroke="#fff" stroke-width="1.3"/><polyline points="4.3,7.7 6.6,10 10.8,5" fill="none" stroke="#fff" stroke-width="1.5"/></svg>Driver decision making</li>
      <li class="topics__item"><svg viewBox="0 0 15 15"><circle cx="7.5" cy="7.5" r="6.5" fill="none" stroke="#fff" stroke-width="1.3"/><polyline points="4.3,7.7 6.6,10 10.8,5" fill="none" stroke="#fff" stroke-width="1.5"/></svg>Research in sign legibility</li>
      <li class="topics__item"><svg viewBox="0 0 15 15"><circle cx="7.5" cy="7.5" r="6.5" fill="none" stroke="#fff" stroke-width="1.3"/><polyline points="4.3,7.7 6.6,10 10.8,5" fill="none" stroke="#fff" stroke-width="1.5"/></svg>Gap acceptance for left turns, right turns, and through movements for drivers, riders, and pedestrians</li>
      <li class="topics__item"><svg viewBox="0 0 15 15"><circle cx="7.5" cy="7.5" r="6.5" fill="none" stroke="#fff" stroke-width="1.3"/><polyline points="4.3,7.7 6.6,10 10.8,5" fill="none" stroke="#fff" stroke-width="1.5"/></svg>Pedestrian walking speeds</li>
      <li class="topics__item"><svg viewBox="0 0 15 15"><circle cx="7.5" cy="7.5" r="6.5" fill="none" stroke="#fff" stroke-width="1.3"/><polyline points="4.3,7.7 6.6,10 10.8,5" fill="none" stroke="#fff" stroke-width="1.5"/></svg>Acceleration</li>
      <li class="topics__item"><svg viewBox="0 0 15 15"><circle cx="7.5" cy="7.5" r="6.5" fill="none" stroke="#fff" stroke-width="1.3"/><polyline points="4.3,7.7 6.6,10 10.8,5" fill="none" stroke="#fff" stroke-width="1.5"/></svg>Lateral acceleration (swerving) for cars, motorcycles, and commercial vehicles</li>
      <li class="topics__item"><svg viewBox="0 0 15 15"><circle cx="7.5" cy="7.5" r="6.5" fill="none" stroke="#fff" stroke-width="1.3"/><polyline points="4.3,7.7 6.6,10 10.8,5" fill="none" stroke="#fff" stroke-width="1.5"/></svg>Forward and backward acceleration of cars, motorcycles and commercial vehicles</li>
      <li class="topics__item"><svg viewBox="0 0 15 15"><circle cx="7.5" cy="7.5" r="6.5" fill="none" stroke="#fff" stroke-width="1.3"/><polyline points="4.3,7.7 6.6,10 10.8,5" fill="none" stroke="#fff" stroke-width="1.5"/></svg>Drivers’ responses to green and yellow traffic signals, deceleration choice, reaction time and probability of stopping</li>
    </ul>
  </section>
</article>
</body>
</html>
```